UX Design for Analytics Web Application

http://tovelunigroup.com/
We are tech & consulting company with analytics products (web applications), located at Rio de Janeiro, Brazil.

We are searching a partner do develop UX for our products, i.e, aesthetics, usability, HTML/CSS.

Currently we have a product suite and the goal is to make a pilot re-design project with one of our products.

The product of interest is interactive webapp that aims at data analysis, significantly different from blogs, e-commerce or landing pages.

We do have a software development team but we lack an UX & HTML expert. Currently we use Bootstrap templates but the results are insatisfatory.

So, the project scope is, to develop the arts (UX, aesthetics, etc) along with the code/mockup (HTML/CSS) for one of our product (3 pages).

This is a pilot project and there's potential to rehire for our other products. Code quality is of importance.

More details and specification can be found in attached files.

Target Market(s)

Executives, managers & consultants

Industry/Entity Type

It Company

Coding

Coded - Design and coding required

Number of Pages Required

3 page

Font styles to use
Sans Serif

Requirements
Must have
• (see attached files, prefer the pptx version))
• -Responsive
Nice to have
• (see attached files, prefer the pptx version)
Should not have
• -Avoid Green, Red and Yellow colors. They have a meaning of good, bad and average in our products.

```html
<!DOCTYPE html>
<html lang="en">
<head>
<meta charset="utf-8">
<title>Analytics Dashboard</title>
<link href="https://fonts.googleapis.com/css2?family=Roboto:wght@300;400;500&display=swap" rel="stylesheet">
<style>
  :root {
    --bg: #f1f1f1;
    --surface: #ffffff;
    --ink: #333333;
    --ink-soft: #555555;
    --muted: #888888;
    --rule: #e6e6e6;
    --azure: #2f8fe0;
    --azure-fill: #e8f2fc;
    --violet: #8a63d2;
    --violet-fill: #f3effb;
    --indigo: #3f51b5;
    --indigo-fill: #eceefa;
    --slate: #5c6b8a;
    --sales: #9779da;
    --badge-one: #6a4fc8;
    --badge-two: #2f8fe0;
  }
  * { box-sizing: border-box; margin: 0; padding: 0; }
  html, body { width: 1200px; height: 690px; overflow: hidden; }
  body {
    background: var(--bg);
    font-family: "Roboto", Arial, sans-serif;
    color: var(--ink);
    position: relative;
  }
  .topbar {
    position: absolute; left: 0; top: 0; width: 1200px; height: 53px;
    background: var(--surface);
    border-bottom: 1px solid var(--rule);
  }
  .topbar .tool { position: absolute; top: 18px; }
  .topbar .mega { position: absolute; left: 236px; top: 17px; font-size: 14px; color: var(--ink); }
  .topbar .lang { position: absolute; left: 804px; top: 17px; font-size: 14px; display: flex; align-items: center; gap: 6px; }
  .flag { width: 16px; height: 11px; display: block; }
  .alert { position: absolute; top: 18px; }
  .badge {
    position: absolute; top: -9px; left: 10px;
    min-width: 18px; height: 18px; border-radius: 9px;
    color: #fff; font-size: 10px; font-weight: 500;
    display: flex; align-items: center; justify-content: center;
  }
  .badge.one { background: var(--badge-one); }
  .badge.two { background: var(--badge-two); }
  .user { position: absolute; left: 1007px; top: 13px; display: flex; align-items: center; gap: 10px; font-size: 14px; }
  .avatar { width: 28px; height: 28px; border-radius: 50%; background: linear-gradient(135deg, #b0a49a, #5e5660); position: relative; }
  .avatar::after { content: ""; position: absolute; right: -1px; bottom: 0; width: 8px; height: 8px; border-radius: 50%; background: var(--azure); border: 1.5px solid #fff; }

  .menubar {
    position: absolute; left: 0; top: 53px; width: 1200px; height: 54px;
    background: var(--surface);
    box-shadow: 0 2px 4px rgba(0,0,0,.06);
    display: flex; align-items: center; padding-left: 85px; gap: 22px;
    font-size: 13.5px; color: var(--ink);
  }
  .menubar a { display: flex; align-items: center; gap: 6px; color: inherit; text-decoration: none; }

  .card { position: absolute; background: var(--surface); }
  .stats { left: 81px; top: 127px; width: 1038px; height: 204px; display: flex; }
  .stat { flex: 1; position: relative; text-align: center; border-right: 1px solid var(--rule); }
  .stat:last-child { border-right: 0; }
  .stat .value { margin-top: 14px; font-size: 29px; font-weight: 400; color: var(--ink-soft); }
  .stat .label { margin-top: 7px; font-size: 12.5px; color: var(--ink-soft); }
  .stat .spark { position: absolute; left: 36px; top: 80px; width: 274px; height: 36px; }
  .stat .split { position: absolute; left: 0; right: 0; top: 140px; display: flex; }
  .stat .split > div { flex: 1; }
  .stat .split > div:first-child { border-right: 1px solid var(--rule); }
  .split .num { font-size: 20px; }
  .split .cap { margin-top: 8px; font-size: 12.5px; color: var(--ink-soft); display: flex; align-items: center; justify-content: center; gap: 5px; }
  .azure .num { color: var(--azure); } .azure .cap svg { stroke: var(--azure); }
  .violet .num { color: var(--violet); } .violet .cap svg { stroke: var(--violet); }
  .indigo .num { color: var(--indigo); } .indigo .cap svg { stroke: var(--indigo); }
  .split .cap svg { fill: none; stroke-width: 1.6; }

  .progress { left: 81px; top: 359px; width: 681px; height: 340px; }
  .legend { position: absolute; top: 22px; left: 0; right: 0; display: flex; justify-content: center; gap: 14px; font-size: 13px; color: var(--ink); }
  .legend span { display: flex; align-items: center; gap: 6px; }
  .dot { width: 11px; height: 11px; border-radius: 50%; display: inline-block; }
  .lines { position: absolute; left: 0; top: 0; width: 681px; height: 280px; }
  .totals { position: absolute; left: 0; top: 278px; width: 681px; border-top: 1px solid var(--rule); display: flex; }
  .totals div { flex: 1; text-align: center; }
  .totals .cap { margin-top: 14px; font-size: 13px; color: var(--ink-soft); }
  .totals .num { margin-top: 2px; font-size: 21px; color: var(--ink); }

  .sales { left: 793px; top: 359px; width: 327px; height: 340px; background: var(--sales); color: #fff; }
  .sales h2 { position: absolute; top: 22px; left: 0; right: 0; text-align: center; font-size: 13.5px; font-weight: 400; }
  .sales svg { position: absolute; left: 0; top: 0; }
  .sales .foot { position: absolute; left: 0; right: 0; top: 306px; border-top: 1px solid rgba(255,255,255,.35); }
</style>
</head>
<body>

<header class="topbar">
  <svg class="tool" style="left:93px" width="20" height="16" viewBox="0 0 20 16" fill="none" stroke="#333" stroke-width="1.8"><path d="M1 2h18M1 8h18M1 14h18"/></svg>
  <svg class="tool" style="left:145px" width="16" height="16" viewBox="0 0 16 16" fill="none" stroke="#333" stroke-width="1.7"><circle cx="6.5" cy="6.5" r="5"/><path d="M10.5 10.5l4 4"/></svg>
  <svg class="tool" style="left:193px" width="16" height="16" viewBox="0 0 16 16" fill="none" stroke="#333" stroke-width="1.6"><path d="M1 5V1h4M11 1h4v4M15 11v4h-4M5 15H1v-4"/></svg>
  <div class="mega">Mega <svg width="9" height="6" viewBox="0 0 9 6" fill="none" stroke="#333" stroke-width="1.3"><path d="M1 1l3.5 3.5L8 1"/></svg></div>

  <div class="lang">
    <svg class="flag" viewBox="0 0 16 11"><rect width="16" height="11" fill="#c8313e"/><path d="M0 1.6h16M0 4.7h16M0 7.8h16" stroke="#fff" stroke-width="1.5"/><rect width="7" height="6" fill="#2d3f7c"/></svg>
    English <svg width="9" height="6" viewBox="0 0 9 6" fill="none" stroke="#333" stroke-width="1.3"><path d="M1 1l3.5 3.5L8 1"/></svg>
  </div>
  <div class="alert" style="left:902px">
    <svg width="16" height="17" viewBox="0 0 16 17" fill="none" stroke="#333" stroke-width="1.5"><path d="M3 12V7a5 5 0 0 1 10 0v5l1.5 1.5h-13zM6.5 15.5a1.6 1.6 0 0 0 3 0"/></svg>
    <span class="badge one">5</span>
  </div>
  <div class="alert" style="left:955px">
    <svg width="17" height="14" viewBox="0 0 17 14" fill="none" stroke="#333" stroke-width="1.5"><rect x="1" y="1.5" width="15" height="11" rx="1"/><path d="M1 2l7.5 6L16 2"/></svg>
    <span class="badge two">8</span>
  </div>
  <div class="user">
    <span class="avatar" role="img" aria-label="User profile photo"></span>
    John Doe <svg width="9" height="6" viewBox="0 0 9 6" fill="none" stroke="#333" stroke-width="1.3"><path d="M1 1l3.5 3.5L8 1"/></svg>
  </div>
</header>

<nav class="menubar">
  <a href="#"><svg width="14" height="13" viewBox="0 0 14 13" fill="#444"><path d="M7 0L0 6h2v7h4V9h2v4h4V6h2z"/></svg>Dashboard</a>
  <a href="#"><svg width="10" height="14" viewBox="0 0 10 14" fill="none" stroke="#444" stroke-width="1.4"><rect x="1" y="1" width="8" height="12" rx="1"/><path d="M4 11h2"/></svg>Mega Menu</a>
  <a href="#"><svg width="14" height="13" viewBox="0 0 14 13" fill="none" stroke="#444" stroke-width="1.4"><rect x="1" y="1" width="12" height="8" rx="1"/><path d="M5 12h4M7 9v3"/></svg>My Menu</a>
  <a href="#"><svg width="14" height="13" viewBox="0 0 14 13" fill="none" stroke="#444" stroke-width="1.4"><rect x="1" y="1" width="12" height="8" rx="1"/><path d="M5 12h4M7 9v3"/></svg>Menu levels</a>
  <a href="#"><svg width="10" height="14" viewBox="0 0 10 14" fill="none" stroke="#444" stroke-width="1.4"><rect x="1" y="1" width="8" height="12" rx="1"/><path d="M4 11h2"/></svg>Mega Menu</a>
  <a href="#"><svg width="14" height="13" viewBox="0 0 14 13" fill="none" stroke="#444" stroke-width="1.4"><rect x="1" y="1" width="12" height="8" rx="1"/><path d="M5 12h4M7 9v3"/></svg>Menu levels</a>
</nav>

<section class="card stats">
  <div class="stat azure">
    <div class="value">$84,962</div>
    <div class="label">Monthly Profit</div>
    <svg class="spark" viewBox="0 0 274 36" preserveAspectRatio="none">
      <path d="M0 14 C20 6 35 8 55 12 S85 22 100 16 S125 10 140 18 S165 24 180 15 S205 22 220 24 S250 12 274 13 V36 H0Z" fill="var(--azure-fill)"/>
      <path d="M0 14 C20 6 35 8 55 12 S85 22 100 16 S125 10 140 18 S165 24 180 15 S205 22 220 24 S250 12 274 13" fill="none" stroke="var(--azure)" stroke-width="1.8"/>
    </svg>
    <div class="split">
      <div><div class="num">$8,200</div><div class="cap"><svg width="10" height="6" viewBox="0 0 10 6"><path d="M1 5l4-4 4 4"/></svg>Today</div></div>
      <div><div class="num">$5,400</div><div class="cap"><svg width="10" height="6" viewBox="0 0 10 6"><path d="M1 1l4 4 4-4"/></svg>Yesterday</div></div>
    </div>
  </div>
  <div class="stat violet">
    <div class="value">1,879</div>
    <div class="label">Total Employee</div>
    <svg class="spark" viewBox="0 0 274 36" preserveAspectRatio="none">
      <path d="M0 14 C15 10 30 20 50 16 S75 12 90 18 S115 14 130 16 S155 10 170 14 S200 12 215 11 S245 0 262 6 L274 10 V36 H0Z" fill="var(--violet-fill)"/>
      <path d="M0 14 C15 10 30 20 50 16 S75 12 90 18 S115 14 130 16 S155 10 170 14 S200 12 215 11 S245 0 262 6 L274 10" fill="none" stroke="var(--violet)" stroke-width="1.8"/>
    </svg>
    <div class="split">
      <div><div class="num">4789</div><div class="cap"><svg width="10" height="6" viewBox="0 0 10 6"><path d="M1 5l4-4 4 4"/></svg>This Quarter</div></div>
      <div><div class="num">389</div><div class="cap"><svg width="10" height="6" viewBox="0 0 10 6"><path d="M1 1l4 4 4-4"/></svg>Last Quarter</div></div>
    </div>
  </div>
  <div class="stat indigo">
    <div class="value">894</div>
    <div class="label">Support Tickets</div>
    <svg class="spark" viewBox="0 0 274 36" preserveAspectRatio="none">
      <path d="M0 14 C15 12 25 20 40 18 S65 10 80 16 S105 12 120 14 S145 20 160 14 S190 10 205 18 S235 6 255 8 L274 14 V36 H0Z" fill="var(--indigo-fill)"/>
      <path d="M0 14 C15 12 25 20 40 18 S65 10 80 16 S105 12 120 14 S145 20 160 14 S190 10 205 18 S235 6 255 8 L274 14" fill="none" stroke="var(--indigo)" stroke-width="1.8"/>
    </svg>
    <div class="split">
      <div><div class="num">81</div><div class="cap"><svg width="10" height="6" viewBox="0 0 10 6"><path d="M1 5l4-4 4 4"/></svg>Critical</div></div>
      <div><div class="num">498</div><div class="cap"><svg width="10" height="6" viewBox="0 0 10 6"><path d="M1 1l4 4 4-4"/></svg>Low</div></div>
    </div>
  </div>
</section>

<section class="card progress">
  <div class="legend">
    <span><i class="dot" style="background:var(--slate)"></i>Remain</span>
    <span><i class="dot" style="background:var(--azure)"></i>Completed</span>
  </div>
  <svg class="lines" viewBox="0 0 681 280">
    <g fill="none" stroke-width="2.6">
      <path stroke="var(--azure)" d="M0 75 C31 75 31 76 62 76 C92 76 92 119 123 119 C154 119 154 150 186 150 C216 150 216 116 247 116 C278 116 278 136 309 136 C340 136 340 83 372 83 C403 83 403 144 434 144 C465 144 465 100 496 100 C527 100 527 160 558 160 C589 160 589 130 620 130 C650 130 650 102 681 90"/>
      <path stroke="var(--slate)" d="M0 196 C31 196 31 244 62 244 C92 244 92 203 123 203 C154 203 154 218 186 218 C216 218 216 200 247 200 C278 200 278 238 309 238 C340 238 340 203 372 203 C403 203 403 218 434 218 C465 218 465 207 496 207 C527 207 527 224 558 224 C589 224 589 214 620 214 C650 214 650 205 681 203"/>
    </g>
    <g fill="#fff" stroke-width="1.8" stroke="var(--azure)">
      <circle cx="1" cy="75" r="3.5"/><circle cx="62" cy="76" r="3.5"/><circle cx="123" cy="119" r="3.5"/><circle cx="186" cy="150" r="3.5"/><circle cx="247" cy="116" r="3.5"/><circle cx="309" cy="136" r="3.5"/><circle cx="372" cy="83" r="3.5"/><circle cx="434" cy="144" r="3.5"/><circle cx="496" cy="100" r="3.5"/><circle cx="558" cy="160" r="3.5"/><circle cx="620" cy="130" r="3.5"/><circle cx="679" cy="91" r="3.5"/>
    </g>
    <g fill="#fff" stroke-width="1.8" stroke="var(--slate)">
      <circle cx="1" cy="196" r="3.5"/><circle cx="62" cy="244" r="3.5"/><circle cx="123" cy="203" r="3.5"/><circle cx="186" cy="218" r="3.5"/><circle cx="247" cy="200" r="3.5"/><circle cx="309" cy="238" r="3.5"/><circle cx="372" cy="203" r="3.5"/><circle cx="434" cy="218" r="3.5"/><circle cx="496" cy="207" r="3.5"/><circle cx="558" cy="224" r="3.5"/><circle cx="620" cy="214" r="3.5"/><circle cx="679" cy="203" r="3.5"/>
    </g>
  </svg>
  <div class="totals">
    <div><div class="cap">Total Projects</div><div class="num">18</div></div>
    <div><div class="cap">Total Task</div><div class="num">125</div></div>
    <div><div class="cap">Completed Task</div><div class="num">242</div></div>
    <div><div class="cap">Total Revenue</div><div class="num">$11,582</div></div>
  </div>
</section>

<section class="card sales">
  <h2>Total monthly Sales.</h2>
  <svg width="327" height="300" viewBox="0 0 327 300">
    <g stroke="rgba(255,255,255,.5)" stroke-width="1">
      <path d="M75 76H285M75 119.5H285M75 163H285M75 206.5H285M75 250H285"/>
    </g>
    <g fill="#fff" font-family="Roboto, Arial, sans-serif" font-size="11" text-anchor="end">
      <text x="58" y="80">3,000</text><text x="58" y="123">2,250</text><text x="58" y="167">1,500</text><text x="58" y="210">750</text><text x="58" y="254">0</text>
    </g>
    <g fill="#fff">
      <rect x="77" y="142" width="5" height="108"/>
      <rect x="95" y="110" width="5" height="140"/>
      <rect x="113" y="166" width="5" height="84"/>
      <rect x="131" y="175" width="5" height="75"/>
      <rect x="148" y="157" width="5" height="93"/>
      <rect x="166" y="126" width="5" height="124"/>
      <rect x="184" y="142" width="5" height="108"/>
      <rect x="202" y="110" width="5" height="140"/>
      <rect x="220" y="166" width="5" height="84"/>
      <rect x="237" y="175" width="5" height="75"/>
      <rect x="255" y="157" width="5" height="93"/>
      <rect x="273" y="126" width="5" height="124"/>
    </g>
    <g fill="#fff" font-family="Roboto, Arial, sans-serif" font-size="11" text-anchor="middle">
      <text x="133" y="271">Apr</text><text x="204" y="271">Aug</text><text x="275" y="271">Dec</text>
    </g>
  </svg>
  <div class="foot"></div>
</section>

</body>
</html>
```